Hospital Website Design - PSD only

We need a web design for a community hospital based in Uniontown, Pennsylvania.

We would like to see a first round of designs for the website HOMEPAGE. Once we have selected finalists for the look & feel, based on the submitted homepage designs, we will request an additional INTERNAL page design.

Both designs should follow the content requirements displayed on the attached wireframes. I will post the internal page wireframe after the homepage design finalists are selected.

The desired Look & Feel for the website is clean and modern.

3 sites we like are:
http://www.marvellcare.org/
http://www.qrtm.org/
http://www.dellwyn.org/

Attached are the Homepage wireframe, and the Brackfield Hospital Logo.

The winning design will communicate a bright, healthy, energetic, community-oriented feeling.

Please note that readability is very important for a hospital website. Font-sizes and line-heights should be carefully selected for comfortable reading.
Updates

Dear designers -- Please don't feel locked into the exact shades of blue / brown used in the logo. We find this color scheme quite ugly and are working on a logo update. The new color scheme will probably still involve some shades of blue and brown, but we aren't sure yet. Please use your best judgement to make a beautiful design, similar in style to the modern / simple aesthetic of http://www.marvellcare.org/ We will be working on feedback to designs today. Thank you.

Regarding Large Rotating Graphic area and Navigation: We prefer a full-width display, rather than boxed. The navigation should be visually prominent, easy to read text that one can scan easily across the top of the page. Again, please refer to http://www.marvellcare.org/ for our preferred design aesthetic. Some of the designs submitted have been somewhat dated in their styling. We'd like a polished, modern, crisp, bold, beautiful design.

Re: choice of image in large rotating graphic area -- Designers, please do not use stock photography of a group of doctors, or a nursing home scene, in your sample rotating graphic areas. Although this should not affect our perception of the design, it throws off everything in the page if we don't like the image. Please try to select a bold / attractive image that you would like to set the tone for your design.

Reason: Extending our deadline to receive more designs exploring other color options containing less brown, or browns with a more attractive vibe. We would also like to see designs that are not exact replicas of the wireframe. The wireframe is just to show the elements on the page. Please use your creativity to utilize these elements in an attractive layout that we will like. We would also prefer to see use of photography that shows a younger, more cheerful, hopeful feeling in the design... and where the photographs are consistent with your design approach. Thanks!

In general, feedback for everyone is, please look here: http://www.marvellcare.org/ that's the feeling / vibe we want. DO NOT let the old, ugly, outdated logo determine your design. We are having the logo redesigned. DO NOT take an ugly, outdated template, and adapt it for this website. We want to see something BEAUTIFUL!!! Please give us your best effort! People who come to this website are in health crisis, and they want to be uplifted!! Their good spirits are in your hands.

Reason: We are still reviewing submissions and working with designers to provide better feedback. Thanks for your patience.

Reason: our sincerest apologies for the failure to provide adequate feedback this week. We hit a snag with the various decision makers on this project and were not able to review the recent submissions. We will make every effort to have a decision by tomorrow. Thank you for your patience.

Target Market(s)

Adults based in suburban & rural community, aged 18-80.

Industry/Entity Type

Hospital

Requirements
Must have
• The design must include all of the content areas outlined on the attached wireframe.
The design must include the attached logo. (Note, we may update the logo during the design contest, but it will not be changed dramatically. It will just be modernized slightly.)
Nice to have
• Show hover states for things like Navigation, Links, or small images in gallery, so we can see how you imagine interactive states.

```html
<!DOCTYPE html>
<html lang="en">
<head>
<meta charset="utf-8">
<title>Brackfield Hospital</title>
<link href="https://fonts.googleapis.com/css2?family=Open+Sans:wght@400;600;700&family=PT+Serif:wght@400;700&display=swap" rel="stylesheet">
<style>
:root{
  --navy:#163f73;
  --blue:#1f5f9f;
  --blue-light:#2f78bf;
  --sky:#e8f0f8;
  --brown:#7a4f26;
  --green:#5c9a2c;
  --green-dark:#477d1e;
  --red:#c7312c;
  --ink:#333;
  --muted:#777;
  --line:#dcdcdc;
  --bg:#ffffff;
  --hero-a:#e8c9a2;
  --hero-b:#b88a5c;
}
*{box-sizing:border-box;margin:0;padding:0}
html,body{width:822px;height:1200px;overflow:hidden}
body{font-family:"Open Sans",Arial,sans-serif;color:var(--ink);background:var(--bg);font-size:10px}
.wrap{width:640px;margin:0 auto;position:relative}
.serif{font-family:"PT Serif",Georgia,serif}

.topbar{height:22px;background:var(--navy);color:#fff;font-size:9px}
.topbar .wrap{display:flex;align-items:center;justify-content:space-between;height:22px}
.topbar .phone{display:flex;align-items:center;gap:5px}
.topbar .tools{display:flex;align-items:center;gap:8px}
.lang{background:var(--red);padding:2px 6px;border-radius:2px;font-size:8px;font-weight:600}

.header{height:88px}
.header .wrap{height:88px;display:flex;align-items:center;justify-content:space-between}
.brand{display:flex;align-items:center;gap:8px}
.brand-mark{width:26px;height:26px;background:var(--blue);border-radius:50%}
.brand-name{font-size:22px;font-weight:700;color:var(--navy);letter-spacing:.5px}
.brand-tag{font-size:8px;color:var(--muted);margin-top:2px}
.util{display:flex;align-items:center;gap:14px}
.util-links{font-size:10px;color:var(--navy);font-weight:600}
.util-links span{color:var(--line);margin:0 4px}
.search{display:flex;border:1px solid var(--line);height:22px}
.search .field{width:110px;padding:4px 6px;color:var(--muted);font-size:9px}
.search .btn{width:22px;background:var(--brown);display:flex;align-items:center;justify-content:center}

.nav{height:28px;background:var(--sky);border-top:1px solid var(--line);border-bottom:3px solid var(--blue)}
.nav ul{list-style:none;display:flex;height:25px;width:640px;margin:0 auto}
.nav li{flex:1;text-align:center;font-size:10px;line-height:25px;color:var(--navy);border-right:1px solid #c9d7e6;font-family:"PT Serif",Georgia,serif}
.nav li.active{background:var(--blue);color:#fff}

.hero{height:328px;position:relative}
.hero .photo{position:absolute;inset:0;width:640px;margin:0 auto;left:0;right:0;background:linear-gradient(100deg,var(--hero-b) 0%,var(--hero-a) 55%,#f3e2cc 100%)}
.caption{position:absolute;left:28px;top:110px;width:262px;background:rgba(190,110,60,.75);color:#fff;padding:10px 14px}
.caption h1{font-size:22px;font-weight:600}
.caption p{font-size:14px;line-height:1.25;margin-top:4px;font-family:"PT Serif",Georgia,serif}
.arrow{position:absolute;top:148px;width:20px;height:30px;background:rgba(0,0,0,.35);display:flex;align-items:center;justify-content:center}
.arrow.prev{left:0}.arrow.next{right:0}
.portal{position:absolute;right:0;top:14px;width:130px;background:var(--green);color:#fff;font-size:9px}
.portal strong{display:block;padding:5px 8px;background:var(--green-dark);font-weight:700}
.portal span{display:block;padding:4px 8px}

.quick{height:96px;border-bottom:1px solid var(--line)}
.quick .wrap{display:flex;align-items:center;height:96px;justify-content:space-between}
.condition h2{font-size:11px;font-weight:700;color:var(--ink);margin-bottom:6px}
.condition .search .field{width:200px}
.condition .search{height:24px}
.actions{display:flex;gap:18px}
.action{width:62px;text-align:center;font-size:9px;color:var(--navy);font-weight:600;line-height:1.2}
.action svg{display:block;margin:0 auto 4px}

.middle{height:260px}
.middle .wrap{display:flex;gap:18px;padding-top:16px}
.section-title{font-size:14px;color:var(--navy);margin-bottom:8px}
.gallery{width:300px}
.gallery-body{display:flex;gap:6px}
.thumbs{display:grid;grid-template-columns:repeat(3,36px);gap:4px}
.thumb{height:36px;background:linear-gradient(135deg,#c9d6e3,#8aa7c4)}
.thumb:nth-child(3n+2){background:linear-gradient(135deg,#e6d2b9,#b79674)}
.thumb:nth-child(4){background:linear-gradient(135deg,#d4e4d0,#8fb08a)}
.video{width:178px;height:116px;background:linear-gradient(135deg,#eef2f6,#b9c7d6);position:relative}
.play{position:absolute;left:71px;top:40px;width:36px;height:36px;border-radius:50%;background:rgba(0,0,0,.45);display:flex;align-items:center;justify-content:center}
.video-bar{position:absolute;left:0;right:0;bottom:0;height:10px;background:rgba(0,0,0,.6)}
.dots{display:flex;gap:4px;margin-top:10px}
.dots i{width:7px;height:7px;border-radius:50%;background:#c9c9c9}
.dots i:first-child{background:var(--blue)}
.visit{width:150px}
.visit ul{list-style:none}
.visit li{font-size:9.5px;line-height:15px;color:var(--ink);display:flex;align-items:center;gap:5px}
.visit li::before{content:"";width:7px;height:7px;border:1px solid #aaa;background:#f4f4f4}
.resources{width:154px;border:1px solid var(--line);background:#f7f9fb;padding:10px}
.resources ul{list-style:none}
.resources li{font-size:9px;line-height:1.35;color:var(--ink);padding:5px 0 5px 10px;border-bottom:1px dotted #ccc;position:relative}
.resources li::before{content:"›";position:absolute;left:0;color:var(--blue);font-weight:700}

.news{height:255px}
.tabs{display:flex;gap:4px;border-bottom:2px solid var(--blue)}
.tab{font-size:12px;padding:6px 16px;background:#eee;color:var(--navy);font-family:"PT Serif",Georgia,serif;border:1px solid var(--line);border-bottom:none}
.tab.active{background:var(--blue);color:#fff;border-color:var(--blue)}
.cards{display:flex;gap:16px;margin-top:18px}
.card{width:148px}
.card .img{height:92px;background:linear-gradient(135deg,#d9e6f2,#8db0cf)}
.card:nth-child(2) .img{background:linear-gradient(135deg,#e6ecf2,#a4b7c9)}
.card:nth-child(3) .img{background:linear-gradient(135deg,#dfe9f0,#7ea3bf)}
.card:nth-child(4) .img{background:linear-gradient(135deg,#e9f2f8,#9bbfd9)}
.card p{font-size:9px;line-height:1.4;margin-top:8px;color:var(--ink)}
.card a{color:var(--blue);font-weight:600;text-decoration:none}

.footer{height:88px;background:var(--blue);color:#fff}
.footer .wrap{display:flex;justify-content:space-between;align-items:center;height:88px}
.footer-links{font-size:9.5px;font-weight:600}
.footer-links span{opacity:.5;margin:0 4px}
.footer-side{display:flex;flex-direction:column;align-items:flex-end;gap:10px}
.awards{background:var(--green);font-size:11px;font-weight:700;letter-spacing:1px;padding:5px 28px;position:relative}
.social{display:flex;gap:6px}
.social i{width:20px;height:20px;border-radius:50%;background:#fff;opacity:.9}
.copy{height:35px;background:var(--navy);color:#cdd9e6;font-size:8.5px}
.copy .wrap{line-height:35px}
</style>
</head>
<body>
<div class="topbar">
  <div class="wrap">
    <div class="phone">
      <svg width="9" height="9" viewBox="0 0 10 10"><path d="M2 1l2 2-1 1.5c.6 1.2 1.3 1.9 2.5 2.5L7 6l2 2-1.3 1.3C4.5 9 1 5.5.7 2.3z" fill="#fff"/></svg>
      (555) 210-4800 | Contact Us
    </div>
    <div class="tools">
      <svg width="10" height="10" viewBox="0 0 10 10"><rect x="1" y="3" width="8" height="5" fill="none" stroke="#fff"/><rect x="3" y="1" width="4" height="2" fill="#fff"/></svg>
      <span>A A A</span>
      <span class="lang">español</span>
    </div>
  </div>
</div>

<header class="header">
  <div class="wrap">
    <div class="brand">
      <div class="brand-mark"></div>
      <div>
        <div class="brand-name serif">Brackfield Hospital</div>
        <div class="brand-tag">Caring for our community since 1902</div>
      </div>
    </div>
    <div class="util">
      <div class="util-links">About Us<span>|</span>News<span>|</span>Giving</div>
      <div class="search">
        <div class="field">Search</div>
        <div class="btn"><svg width="10" height="10" viewBox="0 0 10 10"><circle cx="4" cy="4" r="3" fill="none" stroke="#fff" stroke-width="1.4"/><path d="M6.3 6.3L9 9" stroke="#fff" stroke-width="1.4"/></svg></div>
      </div>
    </div>
  </div>
</header>

<nav class="nav">
  <ul>
    <li class="active">Our Services</li>
    <li>Facilities &amp; Directions</li>
    <li>Patient &amp; Visitor Information</li>
    <li>Find a Doctor</li>
    <li>Health &amp; Wellness</li>
  </ul>
</nav>

<section class="hero">
  <div class="photo" role="img" aria-label="Smiling young patient wearing a headscarf, cancer care feature photo">
    <div class="caption">
      <h1>Cancer Care Center</h1>
      <p>The best doctors and nurses, and treatment close to home.</p>
    </div>
    <div class="arrow prev"><svg width="8" height="12" viewBox="0 0 8 12"><path d="M6 1L1 6l5 5" fill="none" stroke="#fff" stroke-width="2"/></svg></div>
    <div class="arrow next"><svg width="8" height="12" viewBox="0 0 8 12"><path d="M2 1l5 5-5 5" fill="none" stroke="#fff" stroke-width="2"/></svg></div>
    <div class="portal"><strong>Brackfield Patient Portal</strong><span>Login or Register ›</span></div>
  </div>
</section>

<section class="quick">
  <div class="wrap">
    <div class="condition">
      <h2>Do you want to learn about a condition?</h2>
      <div class="search">
        <div class="field">Diabetes, Cancer, Heart Health...</div>
        <div class="btn"><svg width="10" height="10" viewBox="0 0 10 10"><circle cx="4" cy="4" r="3" fill="none" stroke="#fff" stroke-width="1.4"/><path d="M6.3 6.3L9 9" stroke="#fff" stroke-width="1.4"/></svg></div>
      </div>
    </div>
    <div class="actions">
      <div class="action"><svg width="30" height="30" viewBox="0 0 30 30"><path d="M8 4v9a6 6 0 0012 0V4" fill="none" stroke="#1f5f9f" stroke-width="2"/><path d="M14 19v4a4 4 0 008 0v-3" fill="none" stroke="#1f5f9f" stroke-width="2"/><circle cx="22" cy="18" r="2.5" fill="#1f5f9f"/></svg>Symptom Checker</div>
      <div class="action"><svg width="30" height="30" viewBox="0 0 30 30"><path d="M11 3h8M13 3v9l-7 13h18l-7-13V3" fill="none" stroke="#1f5f9f" stroke-width="2"/><path d="M9 20h12l2 5H7z" fill="#1f5f9f"/></svg>Schedule a Lab Test</div>
      <div class="action"><svg width="30" height="30" viewBox="0 0 30 30"><rect x="3" y="7" width="24" height="16" rx="2" fill="none" stroke="#1f5f9f" stroke-width="2"/><rect x="3" y="11" width="24" height="3" fill="#1f5f9f"/><rect x="6" y="17" width="8" height="2" fill="#1f5f9f"/></svg>Online Bill Pay</div>
      <div class="action"><svg width="30" height="30" viewBox="0 0 30 30"><path d="M15 25S4 18 4 11a5 5 0 0111-2 5 5 0 0111 2c0 7-11 14-11 14z" fill="none" stroke="#1f5f9f" stroke-width="2"/></svg>Support our Work</div>
    </div>
  </div>
</section>

<section class="middle">
  <div class="wrap">
    <div class="gallery">
      <h2 class="section-title serif">Watch Our Gallery</h2>
      <div class="gallery-body">
        <div class="thumbs">
          <div class="thumb" role="img" aria-label="Gallery photo"></div>
          <div class="thumb" role="img" aria-label="Gallery photo"></div>
          <div class="thumb" role="img" aria-label="Gallery photo"></div>
          <div class="thumb" role="img" aria-label="Gallery photo"></div>
          <div class="thumb" role="img" aria-label="Gallery photo"></div>
          <div class="thumb" role="img" aria-label="Gallery photo"></div>
          <div class="thumb" role="img" aria-label="Gallery photo"></div>
          <div class="thumb" role="img" aria-label="Gallery photo"></div>
          <div class="thumb" role="img" aria-label="Gallery photo"></div>
        </div>
        <div class="video" role="img" aria-label="Video still of a physician with a patient">
          <div class="play"><svg width="14" height="14" viewBox="0 0 14 14"><path d="M3 1l10 6-10 6z" fill="#fff"/></svg></div>
          <div class="video-bar"></div>
        </div>
      </div>
      <div class="dots"><i></i><i></i><i></i><i></i></div>
    </div>
    <div class="visit">
      <h2 class="section-title serif">About Your Visit</h2>
      <ul>
        <li>Emergency Care</li>
        <li>Accepted Health Plans</li>
        <li>Pre-registration for Surgery</li>
        <li>Lab Hours</li>
        <li>Schedule a Lab Test</li>
        <li>Find a Phone Number</li>
        <li>Find a Form</li>
        <li>Pay Bill Online</li>
        <li>Visitor Guide</li>
      </ul>
    </div>
    <div class="resources">
      <h2 class="section-title serif">Patients Resources</h2>
      <ul>
        <li>Tips on Choosing the Right Doctor</li>
        <li>Billing Forms &amp; Medical Records</li>
        <li>Making the Most of Your Appointment</li>
      </ul>
    </div>
  </div>
</section>

<section class="news">
  <div class="wrap">
    <div class="tabs">
      <div class="tab active">BH News</div>
      <div class="tab">Upcoming Classes &amp; Events</div>
    </div>
    <div class="cards">
      <div class="card"><div class="img" role="img" aria-label="Nurse speaking with a patient"></div><p>Lorem ipsum dolor sit amet, consectetur adipiscing elit. Nulla quam elit. <a>Read More [...]</a></p></div>
      <div class="card"><div class="img" role="img" aria-label="Medical team at work"></div><p>Lorem ipsum dolor sit amet, consectetur adipiscing elit. Nulla quam elit. <a>Read More [...]</a></p></div>
      <div class="card"><div class="img" role="img" aria-label="Doctor reviewing results"></div><p>Lorem ipsum dolor sit amet, consectetur adipiscing elit. Nulla quam elit. <a>Read More [...]</a></p></div>
      <div class="card"><div class="img" role="img" aria-label="Healthy woman outdoors"></div><p>Lorem ipsum dolor sit amet, consectetur adipiscing elit. Nulla quam elit. <a>Read More [...]</a></p></div>
    </div>
  </div>
</section>

<footer class="footer">
  <div class="wrap">
    <div class="footer-links">Referring Physicians<span>|</span>Medical Professionals<span>|</span>Giving<span>|</span>Volunteering<span>|</span>Careers<span>|</span>Online Bill Pay</div>
    <div class="footer-side">
      <div class="awards">AWARDS</div>
      <div class="social"><i></i><i></i><i></i><i></i></div>
    </div>
  </div>
</footer>
<div class="copy"><div class="wrap">Copyright © 2014 Brackfield Hospital</div></div>
</body>
</html>
```